Investment company needing business card

We are wanting a business card which looks sharp and easy on the eye. We are thinking of having a business card with the logo embossed on it, to really make it stand out. We will only have a small amount of information of the business card, person's name, position, email address and phone number

Contact Information for Business Card

Danica Pruett
Executive Assistant
+64 21 547 3162
danicap@harwellcapital.co.nz

Requirements
Must have
• Embossed logo
Should not have
• Not to be busy

```html
<!DOCTYPE html>
<html lang="en">
<head>
<meta charset="utf-8">
<title>Harwell Capital – Business Card</title>
<link rel="stylesheet" href="https://fonts.googleapis.com/css2?family=Lato:wght@400;700;900&display=swap">
<style>
  :root {
    --backdrop: #1c1c1d;
    --card: #333334;
    --card-back: #303031;
    --accent: #2dbd7a;
    --text-soft: #c9c9c9;
    --rule: #6a6a6a;
    --emboss: #3b3b3c;
  }
  * { box-sizing: border-box; margin: 0; padding: 0; }
  html, body {
    width: 1200px;
    height: 1108px;
    overflow: hidden;
    background: var(--backdrop);
    font-family: "Lato", sans-serif;
  }
  .canvas {
    width: 1200px;
    height: 1108px;
    display: flex;
    align-items: center;
    justify-content: center;
    gap: 80px;
  }
  .card {
    width: 400px;
    height: 640px;
    border-radius: 22px;
    position: relative;
  }
  .card--front {
    background: var(--card);
    display: flex;
    flex-direction: column;
    align-items: center;
    padding-top: 150px;
    text-align: center;
  }
  .company-name {
    color: var(--accent);
    font-weight: 900;
    font-size: 38px;
    letter-spacing: 2px;
    line-height: 1.1;
    text-transform: uppercase;
  }
  .company-rule {
    width: 300px;
    height: 1px;
    background: var(--rule);
    margin: 22px 0 60px;
  }
  .person-name {
    color: var(--accent);
    font-weight: 700;
    font-size: 26px;
    letter-spacing: 0.5px;
    text-transform: uppercase;
  }
  .person-role {
    color: var(--text-soft);
    font-size: 17px;
    letter-spacing: 0.5px;
    margin-top: 6px;
    text-transform: uppercase;
  }
  .contact-rule {
    width: 210px;
    height: 1px;
    background: var(--rule);
    margin: 22px 0 24px;
  }
  .contact-line {
    color: var(--text-soft);
    font-size: 18px;
    line-height: 1.5;
  }
  .contact-line--email {
    font-size: 16px;
    text-transform: uppercase;
  }
  .card--back {
    background: var(--card-back);
    display: flex;
    align-items: center;
    justify-content: center;
  }
  .back-mark {
    color: var(--emboss);
    font-weight: 900;
    font-size: 44px;
    letter-spacing: 2px;
    text-transform: uppercase;
    text-align: center;
    line-height: 1.15;
  }
</style>
</head>
<body>
  <main class="canvas">
    <section class="card card--front">
      <h1 class="company-name">Harwell<br>Capital</h1>
      <div class="company-rule"></div>
      <p class="person-name">Danica Pruett</p>
      <p class="person-role">Executive Assistant</p>
      <div class="contact-rule"></div>
      <p class="contact-line">+64 21 547 3162</p>
      <p class="contact-line contact-line--email">danicap@harwellcapital.co.nz</p>
    </section>
    <section class="card card--back">
      <p class="back-mark">Harwell<br>Capital</p>
    </section>
  </main>
</body>
</html>
```